Social Media Infographic for White Paper

Am working on a white paper on social media use by C-Suite Executives, and hope to include some infographics. I would like some help designing the first infographic.

The master bit of information is that "66% of C-Suite Executives use social media for professional purpose."

Within that 66%
-70% post original content on a daily/weekly basis
-13% of professional users are lurkers
-40% plan to use social media even more in the future

After initial design will need to two versions of the infographic, one listing the source at the bottom in small print (Source: 2017 Tollery Partners Executive Social Media Study), the other one with no source information.

Infographic design should be complimentary with my website: www.tollerypartners.example, but use of green should be very limited, if at all.

Target Market(s)

New media, C-Suite Executives, Executive Coaches

Industry/Entity Type

Management Consulting

Font styles to use
Sans Serif

Requirements
Must have
• Infographic with data displayed in a easy to understand format that tells the story of C-Suite Executives that participate in social media for professional purposes.
Nice to have
• Complements website design - www.tollery.example.
Should not have
• Limit use of green from website logo, which can be overpowering. Some is ok, but not too much

```html
<!DOCTYPE html>
<html lang="en">
<head>
<meta charset="utf-8">
<title>C-Suite Executives on Social Media</title>
<link href="https://fonts.googleapis.com/css2?family=Oswald:wght@300;400&family=Open+Sans:wght@400&family=Nunito+Sans:ital,wght@0,300;1,300;1,800&display=swap" rel="stylesheet">
<style>
  :root {
    --bg: #222723;
    --green: #6a9e3f;
    --white: #ffffff;
    --text: #f2f2f2;
    --ring-track: #ffffff;
    --disc-light: #f7f7f7;
    --disc-dark: #d9d9d9;
    --icon: #cfcfcf;
  }
  html, body {
    margin: 0;
    padding: 0;
    width: 1200px;
    height: 1000px;
    overflow: hidden;
    background: var(--bg);
  }
  .infographic {
    position: relative;
    width: 1200px;
    height: 1000px;
    background: var(--bg);
    font-family: "Nunito Sans", Arial, sans-serif;
    color: var(--text);
  }
  .figure {
    position: absolute;
    background: linear-gradient(180deg, #bdbdbd 0%, #ffffff 45%, #e8e8e8 100%);
    border-radius: 40px 40px 6px 6px;
  }
  .figure--woman { left: 282px; top: 148px; width: 108px; height: 180px; }
  .figure--man { left: 752px; top: 120px; width: 116px; height: 192px; }
  .frame {
    position: absolute;
    left: 0; top: 0;
  }
  .headline {
    position: absolute;
    left: 276px;
    width: 616px;
    text-align: center;
  }
  .headline__figure {
    top: 300px;
    font-family: "Oswald", "Arial Narrow", sans-serif;
    font-weight: 400;
    font-size: 206px;
    line-height: 1;
    color: var(--green);
    letter-spacing: -4px;
  }
  .headline__text {
    top: 506px;
    font-family: "Open Sans", Arial, sans-serif;
    font-size: 39px;
    line-height: 53px;
    color: var(--white);
  }
  .gauge {
    position: absolute;
  }
  .stat {
    position: absolute;
  }
  .stat__value {
    font-family: "Oswald", "Arial Narrow", sans-serif;
    font-weight: 300;
    font-size: 70px;
    line-height: 1;
    color: var(--green);
    letter-spacing: -2px;
    margin: 0;
  }
  .stat__label {
    margin: 10px 0 0;
    font-weight: 300;
    font-size: 27px;
    line-height: 34.5px;
    color: var(--text);
  }
  .stat__label em {
    font-style: italic;
    font-weight: 800;
  }
  .stat--content { left: 52px; top: 466px; }
  .stat--future { left: 982px; top: 462px; }
  .stat--lurkers { left: 582px; top: 754px; }
  .divider {
    position: absolute;
    left: 280px;
    top: 934px;
    width: 612px;
    height: 1px;
    background: linear-gradient(90deg, rgba(255,255,255,0) 0%, rgba(255,255,255,0.35) 50%, rgba(255,255,255,0) 100%);
  }
  .source {
    position: absolute;
    left: 276px;
    width: 624px;
    top: 946px;
    text-align: center;
    font-style: italic;
    font-weight: 300;
    font-size: 21px;
    color: var(--green);
    margin: 0;
  }
</style>
</head>
<body>
<main class="infographic">
  <div class="figure figure--woman" role="img" aria-label="White silhouette of a businesswoman reading a tablet"></div>
  <div class="figure figure--man" role="img" aria-label="White silhouette of a businessman reading a tablet"></div>

  <svg class="frame" width="1200" height="1000" viewBox="0 0 1200 1000" aria-hidden="true">
    <defs>
      <linearGradient id="frameStroke" x1="0" y1="0" x2="1" y2="0">
        <stop offset="0" stop-color="#3a3e3b"/>
        <stop offset="0.5" stop-color="#e6e6e6"/>
        <stop offset="1" stop-color="#3a3e3b"/>
      </linearGradient>
      <radialGradient id="disc" cx="0.45" cy="0.4" r="0.65">
        <stop offset="0" stop-color="#ffffff"/>
        <stop offset="1" stop-color="#d6d6d6"/>
      </radialGradient>
      <filter id="glow" x="-30%" y="-30%" width="160%" height="160%">
        <feGaussianBlur stdDeviation="8"/>
      </filter>
    </defs>
    <rect class="frame__outline" x="279" y="282" width="610" height="428" rx="180" fill="var(--bg)" stroke="url(#frameStroke)" stroke-width="5"/>

    <!-- gauge: original content 70% -->
    <g class="gauge-ring" transform="translate(272 478)">
      <circle r="84" fill="#000" opacity="0.55" filter="url(#glow)"/>
      <circle r="78" fill="var(--ring-track)"/>
      <circle r="70" fill="none" stroke="var(--green)" stroke-width="16" pathLength="100" stroke-dasharray="70 30" transform="rotate(144)"/>
      <circle r="58" fill="url(#disc)"/>
      <g fill="none" stroke="var(--icon)" stroke-width="3" stroke-linecap="round">
        <path d="M-24 -32 H10 L22 -20 V32 H-24 Z"/>
        <path d="M-14 -14 H8 M-14 -4 H8 M-14 6 H2"/>
        <path d="M-14 20 q6 -8 10 0 t10 0"/>
        <path d="M30 -26 L6 16"/>
      </g>
    </g>

    <!-- gauge: future use 40% -->
    <g class="gauge-ring" transform="translate(888 500)">
      <circle r="84" fill="#000" opacity="0.55" filter="url(#glow)"/>
      <circle r="78" fill="var(--ring-track)"/>
      <circle r="70" fill="none" stroke="var(--green)" stroke-width="16" pathLength="100" stroke-dasharray="40 60" transform="rotate(-90)"/>
      <circle r="58" fill="url(#disc)"/>
      <g fill="var(--icon)">
        <rect x="-26" y="14" width="12" height="20"/>
        <rect x="-9" y="-2" width="12" height="36"/>
        <rect x="8" y="-20" width="14" height="54"/>
      </g>
      <path d="M-36 -4 Q-14 -6 2 -30" fill="none" stroke="var(--icon)" stroke-width="3"/>
      <path d="M-4 -32 L4 -34 L4 -26 Z" fill="var(--icon)"/>
    </g>

    <!-- gauge: lurkers 13% -->
    <g class="gauge-ring" transform="translate(484 818)">
      <circle r="84" fill="#000" opacity="0.55" filter="url(#glow)"/>
      <circle r="78" fill="var(--ring-track)"/>
      <circle r="70" fill="none" stroke="var(--green)" stroke-width="16" pathLength="100" stroke-dasharray="13 87" transform="rotate(-80)"/>
      <circle r="58" fill="url(#disc)"/>
      <path d="M-46 0 Q0 -44 46 0 Q0 44 -46 0 Z" fill="#e2e2e2"/>
      <circle r="20" fill="#f4f4f4" stroke="var(--icon)" stroke-width="4"/>
      <circle r="9" fill="var(--icon)"/>
    </g>
  </svg>

  <div class="headline headline__figure">66%</div>
  <p class="headline headline__text" style="margin:0">of C-Suite Executives<br>use social media for<br>professional purpose.</p>

  <section class="stat stat--content">
    <p class="stat__value">70%</p>
    <p class="stat__label">post <em>original<br>content</em> on a<br>daily/weekly<br>basis</p>
  </section>

  <section class="stat stat--future">
    <p class="stat__value">40%</p>
    <p class="stat__label">plan to use<br>social media<br>even more in<br>the future</p>
  </section>

  <section class="stat stat--lurkers">
    <p class="stat__value">13%</p>
    <p class="stat__label">of professional<br>users are <em>lurkers</em></p>
  </section>

  <div class="divider"></div>
  <p class="source">Source: 2017 Tollery Partners Executive Social Media Study</p>
</main>
</body>
</html>
```